Design some Business Cards for Vellor Motion

Vellor Motion, an automation design and services company specializing in packaging equipment in manufacturing facilities is in need of an updated business card design. I've got 3 different variations on the logo which I've attached. The primary hex colors are:

53D41D >> green
666666 >> grey

For the business cards, we'd like a 2-sided card. The info side should include:
- employee name
- title
- company name
- company address (6120 Fenwick Court, Alder Falls, OR 97340)
- phone (both +1.541.555.0143 and 800.555.0178)
- e-mail

The web address [login to view URL] should appear somewhere on the card but I'll leave it up to you for the placement.

The color green should be highlighted on at least one side of the card. The logo cannot be altered in color or layout from the files provided.

PLEASE LIMIT YOUR SUBMISSIONS TO A MAXIMUM OF 12 DESIGNS.

I look forward to seeing the results.

Thanks in advance,
Marlene

```html
<!DOCTYPE html>
<html lang="en">
<head>
<meta charset="utf-8">
<title>Vellor Motion — Business Cards</title>
<link rel="stylesheet" href="https://fonts.googleapis.com/css2?family=Roboto:wght@300;400;500&display=swap">
<style>
  :root {
    --green: #53d41d;
    --green-light: #7fe04f;
    --green-deep: #43b516;
    --grey: #666666;
    --grey-light: #8a8a8a;
    --white: #ffffff;
    --page: #ecece8;
  }
  * { box-sizing: border-box; margin: 0; padding: 0; }
  html, body {
    width: 1200px;
    height: 912px;
    overflow: hidden;
    background: var(--page);
    font-family: "Roboto", Arial, sans-serif;
  }
  .sheet {
    position: relative;
    width: 1200px;
    height: 912px;
  }
  .card {
    position: absolute;
    left: 240px;
    width: 720px;
    height: 412px;
    overflow: hidden;
    border-radius: 4px;
    background: linear-gradient(160deg, var(--green-light) 0%, var(--green) 45%, var(--green-deep) 100%);
    box-shadow: 0 10px 24px rgba(0, 0, 0, 0.18);
  }
  .card--back { top: 36px; }
  .card--front { top: 464px; }

  .band {
    position: absolute;
    left: 0;
    width: 100%;
  }
  .band--white {
    background: var(--white);
    border-top: 3px solid rgba(255,255,255,0.6);
  }
  .band--grey {
    background: var(--grey);
    border-bottom: 4px solid var(--white);
  }

  .card--back .band--white { top: 110px; height: 110px; }
  .card--front .band--grey { top: 30px; height: 78px; }
  .card--front .band--white { top: 108px; height: 100px; }

  .brand {
    position: absolute;
    display: flex;
    align-items: center;
    gap: 14px;
  }
  .brand__mark {
    width: 46px;
    height: 46px;
    border-radius: 50%;
    background: var(--grey-light);
    flex: none;
  }
  .brand__name {
    color: var(--green);
    font-weight: 500;
    font-size: 46px;
    letter-spacing: 2px;
    text-transform: uppercase;
    line-height: 1;
  }
  .card--back .brand { left: 170px; top: 140px; }
  .card--front .brand { left: 200px; top: 120px; }
  .card--front .brand__name { font-size: 40px; }
  .card--front .brand__mark { width: 40px; height: 40px; }

  .tagline {
    position: absolute;
    left: 254px;
    top: 172px;
    color: var(--grey-light);
    font-size: 12px;
    font-weight: 400;
    letter-spacing: 5px;
    text-transform: uppercase;
    white-space: nowrap;
  }

  .web {
    position: absolute;
    left: 40px;
    bottom: 40px;
    color: var(--white);
    font-size: 22px;
    font-weight: 400;
  }

  .person {
    position: absolute;
    right: 48px;
    top: 42px;
    text-align: right;
    color: var(--white);
  }
  .person__name {
    font-size: 30px;
    font-weight: 300;
    letter-spacing: 2px;
    text-transform: uppercase;
    line-height: 1.1;
  }
  .person__title {
    font-size: 12px;
    font-weight: 400;
    color: #e2e2e2;
  }

  .contacts {
    position: absolute;
    left: 40px;
    top: 232px;
    list-style: none;
    color: var(--white);
    font-size: 16px;
    line-height: 1.3;
  }
  .contacts__item {
    position: relative;
    padding-left: 26px;
    margin-bottom: 12px;
  }
  .contacts__item::before {
    content: "";
    position: absolute;
    left: 0;
    top: 2px;
    width: 10px;
    height: 20px;
    background: var(--grey);
  }
</style>
</head>
<body>
<main class="sheet">
  <section class="card card--back" aria-label="Card back">
    <div class="band band--white"></div>
    <div class="brand">
      <span class="brand__mark"></span>
      <span class="brand__name">Vellor Motion</span>
    </div>
    <p class="web">www.vellormotion.com</p>
  </section>

  <section class="card card--front" aria-label="Card front">
    <div class="band band--grey"></div>
    <div class="person">
      <p class="person__name">John Doe</p>
      <p class="person__title">Graphic Designer</p>
    </div>
    <div class="band band--white"></div>
    <div class="brand">
      <span class="brand__mark"></span>
      <span class="brand__name">Vellor Motion</span>
    </div>
    <p class="tagline">Engineered Precision</p>
    <ul class="contacts">
      <li class="contacts__item">6120 Fenwick Court<br>Alder Falls, OR 97340</li>
      <li class="contacts__item">+1.541.555.0143<br>+800.555.0178</li>
      <li class="contacts__item">name@vellormotion.com<br>www.vellormotion.com</li>
    </ul>
  </section>
</main>
</body>
</html>
```